Brackenmoor - Healthcare Brochure - B2B

We need a new brochure design, we're satisfied with the copy but were just looking for complete overhaul of the design. Please see an example of the old design attached. It was just a template we filled out.
Requirements
Nice to have
- The second attachment is an example of a style we like

```html
<!DOCTYPE html>
<html lang="en">
<head>
<meta charset="utf-8">
<title>Brackenmoor – Post-Acute Care Brochure</title>
<link href="https://fonts.googleapis.com/css2?family=Poppins:ital,wght@0,400;0,500;0,600;0,700;0,800;1,400&family=Montserrat:wght@700;800&display=swap" rel="stylesheet">
<style>
  :root{
    --blue:#1f78c8;
    --blue-dark:#1565b0;
    --navy:#0c1c33;
    --ink:#1d1d1f;
    --paper:#ffffff;
    --backdrop:#ececec;
    --rule:#2a2a2a;
  }
  *{box-sizing:border-box;margin:0;padding:0}
  html,body{width:1200px;height:2970px;overflow:hidden}
  body{background:var(--backdrop);font-family:'Poppins',sans-serif;color:var(--ink);position:relative}
  .spread{position:absolute;left:30px;width:1140px;height:881px;background:var(--paper);box-shadow:0 6px 18px rgba(0,0,0,.18);overflow:hidden}
  .spread--inside{top:554px}
  .spread--outside{top:1535px}
  .block{position:absolute}
  .blue{background:var(--blue);color:#fff}
  .photo{position:absolute}
  .heading{font-family:'Montserrat',sans-serif;font-weight:800;letter-spacing:4px;line-height:1}

  /* inside spread */
  .about{left:40px;top:58px;width:310px}
  .about .heading{font-size:29px;color:var(--ink)}
  .about .heading span{display:block;color:var(--blue)}
  .about p{margin-top:14px;font-size:15px;line-height:1.18}
  .promise{left:0;top:360px;width:380px;height:236px;padding:56px 40px 0;font-style:italic;font-size:14.5px;line-height:1.22}
  .vision{left:380px;top:0;width:380px;height:275px;padding:52px 46px 0}
  .vision .heading{font-size:29px;color:#fff}
  .vision p{margin-top:12px;font-style:italic;font-size:15px;line-height:1.18}

  .feature{position:absolute;width:300px;display:flex;gap:14px}
  .feature svg{flex:0 0 66px;height:66px}
  .feature h3{font-size:17.5px;font-weight:600;color:var(--blue);line-height:1.2}
  .feature p{font-size:14.5px;line-height:1.18;margin-top:2px}
  .divider{position:absolute;height:2px;background:var(--rule);width:300px}

  /* outside spread */
  .quote{left:0;top:0;width:380px;height:456px;padding:60px 60px 0 75px;font-size:20.5px;line-height:1.24}
  .quote .mark{font-family:'Montserrat',sans-serif;font-weight:800;font-size:96px;line-height:.6;height:56px}
  .quote .mark--open{margin-left:0}
  .quote .mark--close{text-align:right;margin-top:14px;margin-right:10px}
  .wordmark{display:flex;align-items:center;gap:10px;color:var(--blue);font-weight:500;letter-spacing:1px}
  .wordmark i{display:block;border-radius:50%;background:var(--blue)}
  .contact{left:380px;top:0;width:380px;height:881px;text-align:center}
  .contact .wordmark{position:absolute;left:0;right:0;top:336px;justify-content:center;font-size:32px}
  .contact .wordmark i{width:30px;height:30px}
  .cta{position:absolute;left:32px;top:408px;width:316px;height:66px;background:#000;color:var(--blue);font-weight:600;font-size:26px;line-height:66px;border-radius:0 26px 0 0}
  .contact .intro{position:absolute;left:60px;width:260px;top:490px;font-size:15.5px;line-height:1.1}
  .contact .line{position:absolute;left:0;right:0;font-size:22px;font-weight:600}
  .contact .addr{position:absolute;left:0;right:0;top:750px;font-size:16.5px;line-height:1.2}
  .contact svg{position:absolute;left:178px;width:24px;height:24px}
  .web-bar{position:absolute;top:805px;height:76px;color:#fff;font-family:'Montserrat',sans-serif;font-weight:700;font-size:15px;letter-spacing:2px;text-align:center;line-height:44px}
  .cover{left:760px;top:0;width:380px;height:881px;text-align:center}
  .cover .wordmark{position:absolute;left:0;right:0;top:72px;justify-content:center;font-size:34px}
  .cover .wordmark i{width:34px;height:34px}
  .tagline{position:absolute;left:0;right:0;top:518px;color:var(--blue);font-size:23px;line-height:1.2;letter-spacing:.5px}
  .headline{position:absolute;left:0;right:0;top:596px;font-family:'Montserrat',sans-serif;font-weight:800;font-size:27px;line-height:1.04}
  .banner{position:absolute;left:0;width:358px;top:668px;height:137px;padding-top:18px;font-size:19.5px;line-height:1.2}
  .banner strong{display:block;font-weight:600;font-size:23px;margin-bottom:4px}
</style>
</head>
<body>

<section class="spread spread--inside">
  <div class="block about">
    <h2 class="heading">ABOUT<span>BRACKENMOOR</span></h2>
    <p>At Brackenmoor, we don’t just bridge the gap. We transform the journey into a smooth, seamless experience, from the moment a patient discharges from your facility until their appointment with a primary care physician. For Medicare beneficiaries, that’s life-changing.</p>
  </div>
  <div class="block blue promise">Delivering personalized, seamless care that empowers patients, reduces readmissions, and ensures smooth recovery from healthcare facility to home</div>
  <div class="photo" role="img" aria-label="Photo of doctors and nurses reviewing an x-ray together" style="left:0;top:596px;width:380px;height:285px;background:linear-gradient(135deg,#5b6f86,#2d4a78 55%,#d9dee4)"></div>

  <div class="block blue vision">
    <h2 class="heading">OUR VISION</h2>
    <p>To make the healthcare experience for every patient as fluid, efficient, and compassionate as possible. Through cutting-edge care and seamless coordination, we ensure patients recover faster, stay healthier, and never lose sight of their wellbeing.</p>
  </div>
  <div class="photo" role="img" aria-label="Photo of a clinician writing on a clipboard beside a stethoscope and tablet" style="left:760px;top:0;width:380px;height:275px;background:linear-gradient(135deg,#c9cdd2,#eef0f2 45%,#3e5f95 80%,#8a7a6a)"></div>

  <!-- column 2 features -->
  <div class="feature" style="left:426px;top:346px">
    <svg viewBox="0 0 66 66" fill="none" stroke="#1d1d1f" stroke-width="2"><circle cx="8" cy="8" r="4"/><circle cx="22" cy="8" r="4"/><circle cx="36" cy="8" r="4"/><circle cx="8" cy="22" r="4"/><circle cx="8" cy="36" r="4"/><path d="M28 48V24a4 4 0 0 1 8 0v14l10 2a6 6 0 0 1 5 7l-2 13H32l-8-10"/></svg>
    <div><h3>Seamless Transition</h3><p>We ensure smooth facility-to-home transitions with no gaps in care, prioritizing patient outcomes.</p></div>
  </div>
  <div class="divider" style="left:426px;top:478px"></div>
  <div class="feature" style="left:426px;top:516px">
    <svg viewBox="0 0 66 66" fill="none" stroke="#1d1d1f" stroke-width="2"><path d="M6 4h32v58H6z"/><path d="M14 14h6a4 4 0 0 1 0 8h-6v-10m6 8 8 10m-2-10-6 8"/><path d="M12 42h20M12 50h14"/><path d="M58 44a10 10 0 1 1-3-8m3-4v6h-6"/></svg>
    <div><h3>Prescription Refills</h3><p>We handle refills for noncontrolled prescriptions, ensuring your patients have what they need to recover</p></div>
  </div>
  <div class="divider" style="left:426px;top:680px"></div>
  <div class="feature" style="left:426px;top:716px">
    <svg viewBox="0 0 66 66" fill="none" stroke="#1d1d1f" stroke-width="2"><circle cx="33" cy="22" r="16"/><circle cx="33" cy="22" r="11"/><path d="M33 14v16m4-13h-6a3 3 0 0 0 0 6h4a3 3 0 0 1 0 6h-6"/><path d="M10 36v22m-5-6 5 6 5-6M24 44v18m-5-6 5 6 5-6M42 44v18m-5-6 5 6 5-6M56 36v22m-5-6 5 6 5-6"/></svg>
    <div><h3>Reduced<br>Readmission Risk</h3><p>We handle refills for noncontrolled prescriptions, ensuring your patients have what they need to recover</p></div>
  </div>

  <!-- column 3 features -->
  <div class="feature" style="left:806px;top:346px">
    <svg viewBox="0 0 66 66" fill="none" stroke="#1d1d1f" stroke-width="2"><path d="M14 14h30v30H14z"/><path d="M44 22h10l10 12v10H44"/><circle cx="22" cy="46" r="5"/><circle cx="52" cy="46" r="5"/><path d="M2 22h8M0 30h10M2 38h8M50 24v10h12"/></svg>
    <div><h3>VNA Order Sign-Off</h3><p>We sign off on VNA orders, streamlining the process and ensuring seamless home care coordination.</p></div>
  </div>
  <div class="divider" style="left:806px;top:478px"></div>
  <div class="feature" style="left:806px;top:516px">
    <svg viewBox="0 0 66 66" fill="none" stroke="#1d1d1f" stroke-width="2"><circle cx="33" cy="10" r="5"/><path d="M25 24a8 8 0 0 1 16 0M33 24v8M14 32h38M14 32v8M33 32v8M52 32v8"/><circle cx="14" cy="46" r="4"/><circle cx="33" cy="46" r="4"/><circle cx="52" cy="46" r="4"/><path d="M7 60a7 7 0 0 1 14 0zM26 60a7 7 0 0 1 14 0zM45 60a7 7 0 0 1 14 0z"/></svg>
    <div><h3>Streamlined<br>Referral Process</h3><p>Easily refer patients with a fast, simple process that ensures seamless transitions in care.</p></div>
  </div>
  <div class="divider" style="left:806px;top:680px"></div>
  <div class="feature" style="left:806px;top:716px">
    <svg viewBox="0 0 66 66" fill="none" stroke="#1d1d1f" stroke-width="2"><circle cx="33" cy="33" r="30"/><path d="M18 22h30v20H18zM14 46h38M24 28h8M24 34h8M38 28l4 6 4-6"/></svg>
    <div><h3>Patient Education</h3><p>Empowering patient’s with information to make informed decisions about their health.</p></div>
  </div>
</section>

<section class="spread spread--outside">
  <div class="block blue quote">
    <div class="mark mark--open">“</div>
    <p>Our process is simple, fast, and most importantly: effective. One call, and we take it from there. From your healthcare facility to their home, we’re there every step of the way.</p>
    <div class="mark mark--close">”</div>
  </div>
  <div class="photo" role="img" aria-label="Photo of a doctor talking with a smiling patient in a headscarf" style="left:0;top:456px;width:380px;height:425px;background:linear-gradient(120deg,#e6e8ea,#8b95a3 40%,#3f7fc4 75%,#5a4638)"></div>

  <div class="block contact">
    <div class="photo" role="img" aria-label="Photo of a bright hospital corridor with reception desk" style="left:22px;top:28px;width:337px;height:272px;background:linear-gradient(180deg,#e9eef3,#c8d6e2 60%,#8fa9bd)"></div>
    <div class="wordmark"><i></i>BRACKENMOOR</div>
    <div class="cta">GET IN TOUCH NOW</div>
    <p class="intro">Join us in transforming post-acute care. Let’s make every patient’s transition a story of success.</p>
    <svg viewBox="0 0 24 24" style="top:578px"><circle cx="12" cy="12" r="12" fill="#1d1d1f"/><path d="M8 6c1 0 2 3 1.5 3.5L8.5 10.5c.8 2 2.2 3.4 4 4l1-1c.5-.5 3.5.5 3.5 1.5 0 1.5-1.5 2.5-3 2-3.5-1-6-3.5-7-7-.5-1.5.5-4 1-4z" fill="#fff"/></svg>
    <div class="line" style="top:606px">555-014-2290</div>
    <svg viewBox="0 0 24 24" style="top:642px"><circle cx="12" cy="12" r="12" fill="#1d1d1f"/><path d="M8 7h8v3H8zM6 10h12v6H6zM8 14h8v4H8z" fill="#fff"/></svg>
    <div class="line" style="top:670px">555-014-7731</div>
    <svg viewBox="0 0 24 24" style="top:712px"><path d="M12 1a8 8 0 0 0-8 8c0 6 8 14 8 14s8-8 8-14a8 8 0 0 0-8-8z" fill="#1d1d1f"/><circle cx="12" cy="9" r="3" fill="#fff"/></svg>
    <p class="addr">12 Fernhill Rd, Ste 210,<br>Ashcombe, MA, 02110</p>
    <div class="web-bar" style="left:42px;width:338px;background:var(--blue)">www.brackenmoor.com</div>
  </div>

  <div class="block cover">
    <div class="wordmark"><i></i>BRACKENMOOR</div>
    <div class="photo" role="img" aria-label="Photo of a smiling team of doctors and nurses in white coats and blue scrubs" style="left:-4px;top:150px;width:384px;height:349px;background:linear-gradient(135deg,#f1f3f5,#d8dde2 40%,#3d86cf 75%,#2a64a8)"></div>
    <p class="tagline">BRIDGING GAPS.<br>IMPROVING LIVES.</p>
    <p class="headline">REVOLUTIONIZING<br>POST-ACUTE CARE</p>
    <div class="banner blue"><strong>ONE PATIENT AT A TIME</strong>Because every patient deserves a seamless recovery.</div>
    <div class="web-bar" style="left:0;width:380px;background:var(--navy)">www.brackenmoor.com</div>
  </div>
</section>

</body>
</html>
```